Simple HTML Design Needed

We're looking for a simple yet elegant HTML design that will be used for a custom wordpress theme.

We're fairly open to design ideas, but the final product will incorporate elements from the following examples:

http://www.pixomarl.com/widecanvas/
http://layoutbrook.com/demo/tidewell/
http://www.gluvena.at/themedemo/?theme=orbane

We just need the homepage HTML and CSS; we'll create the rest of the pages, unless you want to go above an beyond.

The most creative design will win!

```html
<!DOCTYPE html>
<html lang="en">
<head>
<meta charset="utf-8">
<title>Logo – Home</title>
<link href="https://fonts.googleapis.com/css2?family=Arimo:wght@400;700&display=swap" rel="stylesheet">
<style>
:root{
  --blue:#1e88e5;
  --blue-dark:#0f3f73;
  --hero-a:#0c2746;
  --hero-b:#2c6fae;
  --ink:#333;
  --muted:#777;
  --light:#eef0f2;
  --dark:#1b1d20;
  --dark-2:#25282c;
  --line:#2f86d6;
  --white:#fff;
}
*{box-sizing:border-box;margin:0;padding:0}
html,body{width:686px;height:1200px;overflow:hidden}
body{font-family:"Arimo",Arial,sans-serif;color:var(--ink);background:var(--white);position:relative;font-size:9px;line-height:1.4}
.wrap{position:absolute;left:43px;right:43px}
.topbar{position:absolute;top:0;left:0;right:0;height:18px;background:#f6f6f6;border-bottom:1px solid #e3e3e3}
.topbar .wrap{top:4px;font-size:8px;color:var(--muted)}
.header{position:absolute;top:18px;left:0;right:0;height:54px;background:var(--white)}
.logo{position:absolute;left:43px;top:10px;font-size:28px;font-weight:700;color:var(--blue-dark)}
.nav{position:absolute;right:43px;top:16px;display:flex;gap:4px;list-style:none}
.nav li{font-size:9px;padding:6px 9px;color:#555;position:relative}
.nav li.active{background:var(--blue);color:var(--white)}
.dropdown{position:absolute;left:0;top:24px;width:96px;background:var(--white);border:1px solid #ddd;list-style:none;z-index:3;box-shadow:0 2px 4px rgba(0,0,0,.15)}
.dropdown li{padding:5px 7px;font-size:7px;color:#555;border-bottom:1px solid #eee}
.dropdown li.on{color:var(--blue)}
.hero{position:absolute;top:72px;left:0;right:0;height:252px;background:radial-gradient(ellipse at 60% 40%,var(--hero-b),var(--hero-a) 80%);overflow:hidden}
.hero-caption{position:absolute;left:60px;top:70px;width:255px;padding:10px 12px;background:rgba(0,0,0,.25);color:var(--white)}
.hero-caption h1{font-size:24px;letter-spacing:1px;margin-bottom:8px}
.hero-caption p{font-size:14px;font-weight:700;line-height:1.35}
.hero-device{position:absolute;left:330px;top:28px;width:250px;height:200px;border-radius:4px;background:linear-gradient(180deg,#2a2d33,#101215)}
.arrow{position:absolute;top:110px;width:16px;height:30px;background:rgba(0,0,0,.45)}
.arrow.l{left:0}.arrow.r{right:0}
.rule{position:absolute;left:0;right:0;height:4px;background:var(--line)}
.features{position:absolute;top:328px;left:0;right:0;height:210px;background:var(--light)}
.feature{position:absolute;top:28px;width:180px;text-align:center}
.feature .icon{width:42px;height:42px;margin:0 auto 8px;border-radius:50%;background:var(--white);border:1px solid #d5d8dc;display:flex;align-items:center;justify-content:center}
.feature h3{font-size:11px;color:var(--blue);margin-bottom:5px}
.feature p{font-size:8px;color:var(--muted);margin-bottom:8px}
.btn{display:inline-block;background:var(--blue);color:var(--white);font-size:8px;padding:4px 12px}
.about{position:absolute;top:542px;left:0;right:0;height:236px;background:var(--dark)}
.about h2{font-size:14px;color:var(--white);font-weight:700;margin-bottom:10px;padding-bottom:6px;border-bottom:1px solid #3a3d42}
.who{position:absolute;left:72px;top:18px;width:300px;color:#bbb;font-size:8px}
.who p{margin-bottom:10px}
.testi{position:absolute;left:400px;top:18px;width:215px}
.quote{position:relative;background:var(--dark-2);border:1px solid #3a3d42;padding:10px;color:#f0b400;font-size:8px}
.quote:after{content:"";position:absolute;left:20px;bottom:-7px;border:7px solid transparent;border-bottom:0;border-top-color:var(--dark-2)}
.author{margin-top:14px;color:#bbb;font-size:8px;padding-left:10px}
.projects{position:absolute;top:782px;left:0;right:0;height:196px;background:var(--light)}
.projects h2{position:absolute;left:72px;top:16px;font-size:13px;color:var(--blue)}
.filters{position:absolute;right:72px;top:18px;display:flex;gap:10px;list-style:none;font-size:7px;color:#555}
.filters li.on{color:var(--blue)}
.thumbs{position:absolute;left:72px;right:72px;top:40px;height:126px;display:flex;gap:8px}
.thumb{flex:1;position:relative;border:3px solid var(--white)}
.thumb .bar{position:absolute;left:0;right:0;bottom:10px;height:18px;background:var(--blue);color:var(--white);font-size:8px;font-weight:700;padding:4px 6px}
.footer{position:absolute;top:982px;left:0;right:0;height:196px;background:var(--dark);color:#aaa}
.col{position:absolute;top:18px}
.col h4{font-size:11px;color:var(--white);margin-bottom:8px;padding-bottom:5px;border-bottom:1px solid #3a3d42}
.col p{font-size:8px}
.post{display:flex;gap:6px;margin-bottom:8px;font-size:7px}
.post i{width:26px;height:22px;background:#3a3d42;flex:none}
.contact p{display:flex;gap:6px;align-items:center;margin-bottom:5px}
.copy{position:absolute;top:1178px;left:0;right:0;height:22px;background:#131416;color:#888;font-size:7px}
.copy .wrap{top:7px;left:72px}
</style>
</head>
<body>
<div class="topbar"><div class="wrap">Email: info@samplesite.com</div></div>

<header class="header">
  <div class="logo">Logo</div>
  <ul class="nav">
    <li class="active">Home</li>
    <li>About Us</li>
    <li>Portfolio
      <ul class="dropdown">
        <li>Full Gallery</li>
        <li class="on">Company Website</li>
        <li>Pages</li>
        <li>Clients Testimonials</li>
      </ul>
    </li>
    <li>Blog</li>
    <li>Contact</li>
  </ul>
</header>

<section class="hero">
  <div class="arrow l"></div>
  <div class="hero-caption">
    <h1>Sed Do Eiusmod</h1>
    <p>tempor incididunt ut labore et dolore magna aliqua</p>
  </div>
  <div class="hero-device" role="img" aria-label="Laptop and monitor showing website screens"></div>
  <div class="arrow r"></div>
</section>
<div class="rule" style="top:324px"></div>

<section class="features">
  <div class="feature" style="left:72px">
    <div class="icon"><svg width="20" height="20" viewBox="0 0 20 20"><path d="M7 2h6M8 2v6l-4 9h12l-4-9V2" fill="none" stroke="#555" stroke-width="1.5"/></svg></div>
    <h3>Lorem ipsum dolor sit</h3>
    <p>Duis aute irure dolor in reprehenderit in voluptate velit esse cillum dolore eu fugiat nulla pariatur excepteur sint occaecat cupidatat.</p>
    <span class="btn">Read more</span>
  </div>
  <div class="feature" style="left:253px">
    <div class="icon"><svg width="20" height="20" viewBox="0 0 20 20"><rect x="5" y="2" width="10" height="16" rx="1.5" fill="none" stroke="#555" stroke-width="1.5"/><circle cx="10" cy="15.5" r="1" fill="#555"/></svg></div>
    <h3>Lorem ipsum dolor sit</h3>
    <p>Duis aute irure dolor in reprehenderit in voluptate velit esse cillum dolore eu fugiat nulla pariatur excepteur sint occaecat cupidatat.</p>
    <span class="btn">Read more</span>
  </div>
  <div class="feature" style="left:434px">
    <div class="icon"><svg width="20" height="20" viewBox="0 0 20 20"><path d="M17 3L8 12M8 12l-3 1-2 4 4-2 1-3" fill="none" stroke="#555" stroke-width="1.5"/></svg></div>
    <h3>Lorem ipsum dolor sit</h3>
    <p>Duis aute irure dolor in reprehenderit in voluptate velit esse cillum dolore eu fugiat nulla pariatur excepteur sint occaecat cupidatat.</p>
    <span class="btn">Read more</span>
  </div>
</section>
<div class="rule" style="top:538px"></div>

<section class="about">
  <div class="who">
    <h2>Who we are</h2>
    <p>Lorem ipsum dolor sit amet, consectetur adipisicing elit, sed do eiusmod tempor incididunt ut labore et dolore magna aliqua. Ut enim ad minim veniam, quis nostrud exercitation ullamco laboris nisi ut aliquip ex ea commodo consequat.</p>
    <p>Sed ut perspiciatis unde omnis iste natus error sit voluptatem accusantium doloremque laudantium, totam rem aperiam eaque ipsa quae ab illo inventore.</p>
  </div>
  <div class="testi">
    <h2>Testimonials</h2>
    <div class="quote">Sed ut perspiciatis unde omnis iste natus error sit voluptatem accusantium doloremque laudantium totam rem aperiam.</div>
    <div class="author">Marten Olvik, Brightfold Co</div>
  </div>
</section>
<div class="rule" style="top:778px"></div>

<section class="projects">
  <h2>Latest Projects</h2>
  <ul class="filters">
    <li class="on">All Projects</li><li>Web Design</li><li>Logo Design</li><li>SEO</li><li>Illustrations</li>
  </ul>
  <div class="thumbs">
    <div class="thumb" role="img" aria-label="Vintage red car photo" style="background:linear-gradient(160deg,#c9b89a,#8a3b26)"></div>
    <div class="thumb" role="img" aria-label="Metallic abstract sculpture photo" style="background:linear-gradient(160deg,#d6d6d6,#5c5c5c)"><div class="bar">Lorem ipsum dolor</div></div>
    <div class="thumb" role="img" aria-label="Abstract folded shapes artwork" style="background:linear-gradient(160deg,#e8e2d6,#8c7f6a)"></div>
    <div class="thumb" role="img" aria-label="Sports car on dark background" style="background:linear-gradient(160deg,#2c3a3a,#0d1112)"></div>
  </div>
</section>

<footer class="footer">
  <div class="col" style="left:72px;width:160px">
    <h4>About Us</h4>
    <p>Lorem ipsum dolor sit amet, consectetur adipisicing elit. Nemo enim ipsam voluptatem quia voluptas sit aspernatur aut odit aut fugit.</p>
  </div>
  <div class="col" style="left:258px;width:170px">
    <h4>From the Blog</h4>
    <div class="post"><i></i><span>Quis autem vel eum iure<br>Jan 12, 2013</span></div>
    <div class="post"><i></i><span>Quis autem vel eum iure<br>Jan 12, 2013</span></div>
    <div class="post"><i></i><span>Quis autem vel eum iure<br>Jan 12, 2013</span></div>
  </div>
  <div class="col contact" style="left:455px;width:160px">
    <h4>Contact Us</h4>
    <p><svg width="8" height="10" viewBox="0 0 8 10"><path d="M4 10S0 5.5 0 4a4 4 0 018 0c0 1.5-4 6-4 6z" fill="#aaa"/></svg>No 12 Sample Street, Harbour City</p>
    <p><svg width="8" height="10" viewBox="0 0 8 10"><rect x="1" y="0" width="6" height="10" rx="1" fill="#aaa"/></svg>+1 555 0134 200</p>
    <p><svg width="8" height="10" viewBox="0 0 8 10"><rect y="2" width="8" height="6" fill="#aaa"/></svg>info@samplesite.com</p>
    <p><svg width="8" height="10" viewBox="0 0 8 10"><rect x="1" y="0" width="6" height="10" rx="1" fill="#aaa"/></svg>+1 555 0134 201</p>
  </div>
</footer>
<div class="copy"><div class="wrap">© 2013 samplesite. All Rights Reserved.</div></div>
</body>
</html>
```